Slideshow for exhibition of a new financial trading engine solution

I want a slideshow promoting zTRX, a new trading engine solution.

Basic text content and a loose structure are provided. I want you to come up with a way to GRAPHICALLY ENHANCE the message. Please go beyond mere copy-and-paste jobs.

Target:
- single monitor display
- no sound/audio
- 90-120 seconds
- 10-15 slides
- use graphics to enhance message
- improve on diagrams
- animated
- any format
- targeted for professionals

We have built zTRX (a new trading engine solution platform) boasting significantly FASTER SPEEDS for both data feeds and trading systems.

We want to convey that we have a powerful trading engine solution featuring:
Fast streaming full tick data feed = providing live market updates.
Fast trading system = faster order processing ability.

Slide 1
- Quorel Logo
- zTRX – the Next-Generation Trading Solution

Slide 2 – Why does PLMx Vesper matter to retail markets?
· Vesper transforms the landscape of trading platforms through new technology.
· Necessary to update systems to keep up with the industry standard.
· Retail markets that fail to upgrade may face being left behind by competitors.

Slide 3 – Background of PLMx Vesper Platform
· The PLMx’s Vesper Core Relay Platform is a transformative programme that aims to revolutionise PLMx’s core trading platforms through combining a new platform with new facilities.
· Its efficient and high capacity architecture provides centralised, low-latency and resilient access to PLMx’s securities market.

Slide 4 – What will happen to retail investors under the new platform?
· To operate in a highly competitive marketplace driven by speed, new technologies and revenue, both powerful execution and price improvements are essential to market participants.
· Without an up-to-date trading engine there is the possibility of optimisation problems, and the chance of being unable to get the best price and losing competitiveness.

Slide 5
· Due to the new platform, not having an up-to-date trading engine may lead to issues of being left behind, optimisation and compatibility.
· Orders from retail investors may suffer from increased delays and take a longer time to be placed in the order queue.
· The end result is transactions may be matched with non-competitive prices.

Slide 6 – Quorel’s role
· At Quorel, we aim to level the playing field and allow retail markets to compete with more investment-focused markets. To achieve this we have created a new zTRX trading engine solution.

Slide 7 – zTRX
· zTRX is our new trading system that combines ultra low-latency with dedicated compatibility and optimisation.
· This new architecture takes full advantage of the Vesper platform’s potential to deliver advantages in speed, reliability and precision.

Slide 8
· The key benefit of zTRX is its ability to:-
o Catch the best price: instantaneously track the rapid streaming price fluctuations sent from the PLMx Equities Deep-stream (ED) datafeed, and
o Queue the order at PLMx more quickly: process and send orders within 0.005s (5 milliseconds).

Slide 9
· Fast zTRX trading engine solution + PLMx ED datafeed

Slide 10
· Compatibility
o Designed to take full advantage of PLMx’s ultra-fast Equities Deep-stream (ED) datafeed.
o Employs cutting-edge technology to operate at its peak within the Vesper platform.
· Optimisation
o Efficient use of co-location facilities at PLMx’s centralized Pak Lam Wan Commerce Park data centre.
o Utilise the gains of co-benefit of full-tick streaming quotes and up-to-the-millisecond order processing.
o Maximise speed of a single ‘in memory’ data infrastructure through the entire trade lifecycle.

Slide 11 – Key Features
· Integrated with Wave, Basket and Bulk Order Management.
· Centralised order types for program trade.
· Provision of a rich set of exchange connectivity.
· Comprehensive risk management.
· Extensive interactivity, customization, filtering and search capabilities.
· Bilingual support (English and Chinese).

Slide 12 – About Quorel
· At Quorel, we pride ourselves on providing high quality award-winning products that both adapt to changing technology standards and provide market-leading performance. zTRX is no different, and adheres to our philosophy of providing an innovative and superior product.

Slide 13 – Quorel – your one-stop service provider
· Quorel offers an award-winning combination of real time financial information coverage and trading solution integrated across the front, middle and back office - all in one customizable platform that active investors demand. From spotting new trading opportunities, through to portfolio management, Quorel offers innovative and needs-based solutions to help banks and securities firms.

Slide 14
· middle and back-office system – zLedger
· front-office system – zTRX
· remote channel trading – zNet and Mobile
· financial information terminal – zTrader
· market information portal – zGate

Background Information (for your understanding only):

Our website is http://www.quorelfx.example/

The stock exchange is launching a new platform that will further its position as a leading global exchange. Our company is developing a new trading solution for retail corporations (banks and brokerages) to allow them to cope with the exchange’s new platform.

Our aim is to level the playing field for retail markets by providing a fast streaming full tick data feed and an extremely fast trading engine with the average processing speed of around 1 millisecond per transaction. Thus, it allows retail orders get into the queue faster compared to the traditional trading platform.

A data feed is used to collect data from the financial market. The two forms of data feed are “snapshot” and “streaming”. A snapshot feed only provides a static view of the data at a particular time. A streaming (“full tick”) feed can view the data in real-time and track its fluctuations. Our data feed is a fast streaming feed providing the most up-to-the-millisecond information possible. Our point is our engine can take advantage of this through superior handling, compression, batching and integration.

A trading system is used by financial institutions to process trades. Our trading system is able to react faster and take advantage of fast data feeds. The speed at which a trade is processed determines its “position in the queue”. Having a better position in the queue is advantageous, as the trade will be handled earlier than the one behind. Assuming two trading systems receive the same market data simultaneously, the faster trading system will be able to process it quicker and gain a better position in the queue. Our system can execute an order in a matter of milliseconds.

For example, take an automated buy/sell order for a share. Our fast streaming data feed can monitor the share price in real-time. When the price meets the order level, our fast trading system will then process the trade quicker than its competitors, resulting in a better position in the queue for trading.

Updates:
Due to the complexity of the project, submissions and drafts will be frequently monitored and feedback provided to ensure that they are moving in the desired direction. The definition may also be rewritten as required.
Updates

Thank you all for your submissions thus far. We are in the process of writing up a basic slideshow outline, with headings and content. These will be posted in a subsequent update.

We are looking for you to create or utilise visual designs and effects in the slideshow to enhance the viewer's understanding of the content.

The desired text structure of the slideshow will be updated in the brief today.

Project Deadline Extended

Target Market(s)

Retail banks and brokers

Industry/Entity Type

Architecture

Requirements
Must have
• At least basic animation.
Should not have
• Sound/audio.

```html
<!DOCTYPE html>
<html lang="en">
<head>
<meta charset="utf-8">
<title>Quorel zTRX Slide Template</title>
<link rel="stylesheet" href="https://fonts.googleapis.com/css2?family=Open+Sans:wght@400;600;700&family=Arimo:wght@400;700&display=swap">
<style>
  :root {
    --brand-blue: #2a69c3;
    --header-light: #f3f8fe;
    --header-mid: #d9e8f8;
    --header-deep: #bcd5f1;
    --rule-light: #a9c8f0;
    --rule-blue: #4a82d6;
    --rule-low: #6c9be0;
    --body-top: #ffffff;
    --body-mid: #e8f1fb;
    --body-low: #f4f8fd;
    --text-dark: #1a1a1a;
    --text-body: #333333;
    --footer-left: #2e6bc8;
    --footer-right: #6ea0e6;
    --visual-deep: #08205a;
    --visual-mid: #0f4aa8;
    --visual-bright: #1c8de6;
    --visual-glow: #6fd0ff;
    --frame: #ffffff;
  }
  * { margin: 0; padding: 0; box-sizing: border-box; }
  html, body { width: 1200px; height: 900px; overflow: hidden; background: #ffffff; }

  .slide {
    position: relative;
    width: 1200px;
    height: 900px;
    overflow: hidden;
    background: linear-gradient(180deg, var(--body-top) 28%, var(--body-mid) 68%, var(--body-low) 100%);
    font-family: "Open Sans", Arial, sans-serif;
  }
  .body-backdrop {
    position: absolute;
    left: 600px; top: 255px;
    width: 600px; height: 200px;
    background: radial-gradient(ellipse at 60% 20%, rgba(170,200,235,0.45) 0%, rgba(255,255,255,0) 70%);
  }

  .slide-header {
    position: absolute;
    left: 0; top: 0;
    width: 1200px; height: 237px;
    background: linear-gradient(90deg, var(--header-light) 0%, var(--header-mid) 55%, var(--header-deep) 100%);
  }
  .header-backdrop {
    position: absolute;
    right: 0; top: 0;
    width: 480px; height: 237px;
    background: radial-gradient(ellipse at 65% 60%, rgba(230,240,252,0.95) 0%, rgba(190,214,242,0.5) 50%, rgba(255,255,255,0) 85%);
  }
  .brand {
    position: absolute;
    left: 34px; top: 78px;
    display: flex;
    align-items: center;
    gap: 14px;
  }
  .brand-mark {
    width: 30px; height: 30px;
    border-radius: 50%;
    background: var(--brand-blue);
  }
  .brand-name {
    font-weight: 700;
    font-size: 58px;
    line-height: 66px;
    color: var(--text-dark);
  }
  .presentation-title {
    position: absolute;
    right: 22px; top: 90px;
    font-weight: 700;
    font-size: 52px;
    line-height: 72px;
    color: var(--brand-blue);
    white-space: nowrap;
  }
  .header-rule {
    position: absolute;
    left: 0; top: 237px;
    width: 1200px; height: 18px;
    background: linear-gradient(180deg, var(--rule-light) 0%, var(--rule-blue) 20%, var(--rule-low) 100%);
  }

  .content-title {
    position: absolute;
    left: 41px; top: 328px;
    font-family: "Arimo", Arial, sans-serif;
    font-weight: 700;
    font-size: 41px;
    line-height: 50px;
    color: var(--text-dark);
  }
  .content-body {
    position: absolute;
    left: 45px; top: 388px;
    width: 606px;
    font-family: "Arimo", Arial, sans-serif;
    font-size: 21px;
    line-height: 34.6px;
    color: var(--text-body);
  }
  .content-line {
    display: block;
    text-align: justify;
    text-align-last: justify;
    white-space: nowrap;
  }
  .content-line--last { text-align: left; text-align-last: left; }

  .feature-visual {
    position: absolute;
    left: 705px; top: 411px;
    width: 455px; height: 303px;
    border: 3px solid var(--frame);
    box-shadow: 0 1px 4px rgba(0,0,0,0.35);
    background:
      radial-gradient(circle at 40% 60%, var(--visual-glow) 0%, var(--visual-bright) 22%, rgba(28,141,230,0) 60%),
      linear-gradient(135deg, var(--visual-deep) 0%, var(--visual-mid) 50%, var(--visual-deep) 100%);
  }

  .slide-footer {
    position: absolute;
    left: 0; top: 855px;
    width: 1200px; height: 45px;
    background: linear-gradient(90deg, var(--footer-left) 0%, var(--footer-right) 100%);
  }
  .copyright {
    position: absolute;
    left: 20px; top: 10px;
    font-size: 19px;
    line-height: 26px;
    color: #ffffff;
  }
</style>
</head>
<body>
<main class="slide">
  <div class="body-backdrop" role="img" aria-label="Faint market figures fading into the background"></div>

  <header class="slide-header">
    <div class="header-backdrop" role="img" aria-label="Faint globe and binary digits backdrop"></div>
    <div class="brand">
      <span class="brand-mark"></span>
      <span class="brand-name">Quorel</span>
    </div>
    <h1 class="presentation-title">Presentation Title here</h1>
  </header>
  <div class="header-rule"></div>

  <h2 class="content-title">Content Title here</h2>
  <p class="content-body">
    <span class="content-line">Lorem ipsum dolor sit ipsum Lorem ipsum dolor sit</span>
    <span class="content-line">ipsumLorem ipsum dolor sit ipsumLorem ipsum dolor sit</span>
    <span class="content-line">ipsum Lorem ipsum dolor sit ipsum Lorem ipsum dolor sit</span>
    <span class="content-line">ipsumLorem ipsum dolor sit ipsumLorem ipsum dolor sit</span>
    <span class="content-line">ipsumLorem ipsum dolor sit ipsum Lorem ipsum dolor sit</span>
    <span class="content-line">ipsumLorem ipsum dolor sit ipsumLorem ipsum dolor sit</span>
    <span class="content-line">ipsumLorem ipsum dolor sit ipsum Lorem ipsum dolor sit</span>
    <span class="content-line">ipsumLorem ipsum dolor sit ipsumLorem ipsum dolor sit</span>
    <span class="content-line">ipsumLorem ipsum dolor sit ipsum Lorem ipsum dolor sit</span>
    <span class="content-line">ipsumLorem ipsum dolor sit ipsumLorem ipsum dolor sit</span>
    <span class="content-line content-line--last">ipsumLorem ipsum dolor sit ipsum Lorem ipsum.</span>
  </p>

  <div class="feature-visual" role="img" aria-label="Blue digital market chart with a falling arrow over streaming binary digits"></div>

  <footer class="slide-footer">
    <span class="copyright">Copyright text here</span>
  </footer>
</main>
</body>
</html>
```